Android Battery Saver App UI design.

We need a mockup layout design of an Android app uncoded. This simple battery saver app is composed primarily by three screens described in the attached specification. After the mockup approved we need the UI elements sliced, the app icon and a banner for the vendo shelf.

```html
<!DOCTYPE html>
<html lang="en">
<head>
<meta charset="utf-8">
<title>Charge Keeper Pro – App Screens</title>
<link rel="stylesheet" href="https://fonts.googleapis.com/css2?family=Ubuntu:wght@400;500;700&display=swap">
<style>
  :root {
    --bg: #161616;
    --screen: #1c1c1c;
    --bar: #0b0b0b;
    --header: #2a2a2a;
    --tabs: #202020;
    --row: #1d1d1d;
    --row-line: #0f0f0f;
    --green: #6ee81c;
    --green-deep: #3fb80b;
    --white: #f2f2f2;
    --muted: #a9a9a9;
  }
  * { box-sizing: border-box; margin: 0; padding: 0; }
  html, body { width: 1200px; height: 675px; overflow: hidden; }
  body {
    background: var(--bg);
    font-family: "Ubuntu", sans-serif;
    color: var(--white);
    position: relative;
  }
  ul { list-style: none; }
  .screen {
    position: absolute;
    top: 92px;
    width: 260px;
    height: 492px;
    background: var(--screen);
    overflow: hidden;
  }
  .screen--splash { left: 79px; background: radial-gradient(ellipse at 50% 10%, #2a3a18 0%, #1a1a1a 45%, #141414 100%); }
  .screen--info { left: 476px; }
  .screen--power { left: 848px; }

  .status-bar {
    position: absolute; top: 0; left: 0; right: 0; height: 20px;
    background: var(--bar);
    display: flex; align-items: center; justify-content: flex-end; gap: 7px;
    padding-right: 8px; font-size: 11px; font-weight: 500;
  }
  .status-bar svg { display: block; }
  .nav-bar {
    position: absolute; bottom: 0; left: 0; right: 0; height: 38px;
    background: var(--bar);
    display: flex; justify-content: space-around; align-items: center;
  }

  .app-header {
    position: absolute; top: 20px; left: 0; right: 0; height: 36px;
    background: var(--header);
    display: flex; align-items: center; padding-left: 11px;
    font-size: 14px; font-weight: 700; color: var(--green);
  }
  .tabs {
    position: absolute; top: 56px; left: 0; right: 0; height: 28px;
    background: var(--tabs);
    display: flex; align-items: center; white-space: nowrap;
    font-size: 8.5px; color: var(--muted); overflow: hidden;
  }
  .tab { padding: 0 13px; height: 28px; line-height: 28px; position: relative; }
  .tab--active { color: var(--white); }
  .tab--active::after {
    content: ""; position: absolute; left: 8px; right: 8px; bottom: 1px; height: 2px; background: var(--green);
  }
  .tab--clipped { padding-left: 0; }
  .tab--after-clip { margin-left: 8px; }

  /* splash */
  .brand { position: absolute; top: 40px; left: 0; right: 0; text-align: center; font-weight: 700; color: var(--white); }
  .brand__line { font-size: 21px; line-height: 1; }
  .brand__big { font-size: 64px; line-height: 1; margin-top: 4px; }
  .brand__dot { position: absolute; top: 92px; right: 22px; width: 18px; height: 18px; border-radius: 50%; background: var(--green); }
  .tagline { position: absolute; top: 193px; left: 0; right: 0; text-align: center; font-size: 10px; font-weight: 500; color: var(--white); }
  .tagline em { font-style: normal; color: var(--green); }
  .hero-art {
    position: absolute; top: 224px; left: 74px; width: 112px; height: 174px;
    border-radius: 14px;
    background: linear-gradient(180deg, #4fb313 0%, #6ee81c 55%, #3c8f0d 100%);
    opacity: .9;
  }
  .maker { position: absolute; top: 428px; left: 0; right: 0; text-align: center; font-size: 10.5px; font-weight: 500; color: var(--white); }

  /* current info */
  .battery { position: absolute; top: 96px; left: 24px; }
  .drain-ring {
    position: absolute; top: 108px; left: 158px; width: 64px; height: 64px;
    border: 3px solid var(--white); border-radius: 50%;
    display: flex; flex-direction: column; align-items: center; justify-content: center;
    background: #151515;
  }
  .drain-ring__time { font-size: 15px; font-weight: 700; color: var(--green); line-height: 1; }
  .drain-ring__label { font-size: 7px; color: var(--white); margin-top: 2px; }
  .save-button {
    position: absolute; top: 187px; left: 147px; width: 85px; height: 28px;
    background: linear-gradient(180deg, #7cf02a, #4cc812);
    border-radius: 2px; color: #14310a; font-size: 9px; font-weight: 500;
    display: flex; align-items: center; justify-content: center;
  }
  .lower-panel {
    position: absolute; top: 262px; left: 0; right: 0; bottom: 38px;
    background: linear-gradient(180deg, #1f1f1f, #141414);
  }
  .charging { position: absolute; top: 286px; left: 0; right: 0; text-align: center; }
  .charging__label { font-size: 9px; color: var(--white); margin-top: 4px; }
  .charging__time { font-size: 13px; font-weight: 700; color: var(--green); }
  .shortcuts {
    position: absolute; top: 394px; left: 0; right: 0;
    display: flex; justify-content: space-around; padding: 0 2px;
  }
  .shortcut { width: 80px; text-align: center; font-size: 7px; color: var(--white); }
  .shortcut__icon {
    width: 40px; height: 40px; border-radius: 50%; margin: 0 auto 5px;
    background: #0c0c0c; box-shadow: inset 0 0 0 1px #2b2b2b;
    display: flex; align-items: center; justify-content: center;
  }

  /* power management */
  .settings-list { position: absolute; top: 84px; left: 0; right: 0; }
  .setting {
    height: 52px; display: flex; align-items: center;
    background: var(--row); border-bottom: 1px solid var(--row-line);
    padding: 0 15px 0 20px; font-size: 12.5px; font-weight: 500;
  }
  .setting__icon { width: 28px; display: flex; justify-content: center; margin-right: 14px; }
  .setting__name { flex: 1; }
  .slider { position: relative; flex: 1; height: 30px; }
  .slider__label { position: absolute; top: 0; left: 0; font-size: 11px; }
  .slider__track { position: absolute; top: 20px; left: 0; right: 0; height: 1px; background: #666; }
  .slider__knob { position: absolute; top: 13px; width: 15px; height: 15px; border-radius: 50%; background: #e9e9e9; }
  .slider__knob--brightness { left: 52px; }
  .slider__knob--volume { left: 90px; }
  .toggle {
    position: relative; width: 45px; height: 17px; border-radius: 9px;
    font-size: 7px; line-height: 17px;
  }
  .toggle--on { background: var(--green-deep); color: #d8ffc0; padding-left: 6px; }
  .toggle--off { background: #2c2c2c; color: var(--muted); text-align: right; padding-right: 7px; box-shadow: inset 0 0 0 1px #444; }
  .toggle::after {
    content: ""; position: absolute; top: -1px; width: 19px; height: 19px; border-radius: 50%; background: #f4f4f4;
  }
  .toggle--on::after { right: -1px; }
  .toggle--off::after { left: -1px; }
</style>
</head>
<body>

<!-- Splash screen -->
<section class="screen screen--splash">
  <div class="status-bar">
    <svg width="12" height="10" viewBox="0 0 12 10"><rect x="3" y="1" width="6" height="8" rx="1" fill="none" stroke="#ccc"/><path d="M1 3v4M11 3v4" stroke="#ccc"/></svg>
    <svg width="12" height="10" viewBox="0 0 12 10"><path d="M0 10h2V7H0zM3 10h2V5H3zM6 10h2V3H6zM9 10h2V0H9z" fill="#39a0e0"/></svg>
    <svg width="7" height="11" viewBox="0 0 7 11"><rect x="0.5" y="1.5" width="6" height="9" fill="#39a0e0"/><rect x="2" y="0" width="3" height="2" fill="#39a0e0"/></svg>
    <svg width="11" height="11" viewBox="0 0 11 11"><circle cx="5.5" cy="6" r="4.3" fill="none" stroke="#ccc"/><path d="M5.5 3.5V6h2" stroke="#ccc" fill="none"/></svg>
    <span>00:22</span>
  </div>
  <div class="brand">
    <div class="brand__line">Charge Keeper</div>
    <div class="brand__big">Pro</div>
  </div>
  <span class="brand__dot"></span>
  <p class="tagline"><em>Advanced</em> Battery Saver</p>
  <div class="hero-art" role="img" aria-label="Large illustration of a fully charged green battery"></div>
  <p class="maker">Velmora Systems Inc</p>
  <nav class="nav-bar">
    <svg width="12" height="10" viewBox="0 0 12 10"><path d="M0 1h12M0 5h12M0 9h12" stroke="#555" stroke-width="1.3"/></svg>
    <svg width="13" height="12" viewBox="0 0 13 12"><path d="M1 6 6.5 1 12 6M2.5 5v6h8V5" stroke="#555" fill="none" stroke-width="1.3"/></svg>
    <svg width="13" height="10" viewBox="0 0 13 10"><path d="M4 1 1 4l3 3M1 4h8a3 3 0 0 1 0 6" stroke="#555" fill="none" stroke-width="1.3"/></svg>
  </nav>
</section>

<!-- Current info screen -->
<section class="screen screen--info">
  <div class="status-bar">
    <svg width="12" height="10" viewBox="0 0 12 10"><rect x="3" y="1" width="6" height="8" rx="1" fill="none" stroke="#ccc"/><path d="M1 3v4M11 3v4" stroke="#ccc"/></svg>
    <svg width="12" height="10" viewBox="0 0 12 10"><path d="M0 10h2V7H0zM3 10h2V5H3zM6 10h2V3H6zM9 10h2V0H9z" fill="#39a0e0"/></svg>
    <svg width="7" height="11" viewBox="0 0 7 11"><rect x="0.5" y="1.5" width="6" height="9" fill="#39a0e0"/><rect x="2" y="0" width="3" height="2" fill="#39a0e0"/></svg>
    <svg width="11" height="11" viewBox="0 0 11 11"><circle cx="5.5" cy="6" r="4.3" fill="none" stroke="#ccc"/><path d="M5.5 3.5V6h2" stroke="#ccc" fill="none"/></svg>
    <span>00:22</span>
  </div>
  <header class="app-header">Charge Keeper Pro</header>
  <nav class="tabs">
    <span class="tab">HISTORY</span>
    <span class="tab tab--active">CURRENT INFO</span>
    <span class="tab">POWER MANAGEMENT</span>
  </nav>

  <svg class="battery" width="80" height="160" viewBox="0 0 80 160">
    <defs>
      <linearGradient id="cell" x1="0" x2="1">
        <stop offset="0" stop-color="#3fb80b"/><stop offset=".45" stop-color="#7cf52e"/><stop offset="1" stop-color="#3aa80a"/>
      </linearGradient>
      <linearGradient id="cap" x1="0" x2="1">
        <stop offset="0" stop-color="#555"/><stop offset=".5" stop-color="#bbb"/><stop offset="1" stop-color="#555"/>
      </linearGradient>
    </defs>
    <rect x="24" y="0" width="32" height="14" rx="2" fill="url(#cap)"/>
    <rect x="4" y="13" width="72" height="144" rx="4" fill="#2a2a2a" stroke="#3d3d3d"/>
    <path d="M4 44q18-8 36 0t36 0V153a4 4 0 0 1-4 4H8a4 4 0 0 1-4-4z" fill="url(#cell)"/>
  </svg>

  <div class="drain-ring">
    <span class="drain-ring__time">8d 15h</span>
    <span class="drain-ring__label">Untill Drain</span>
  </div>
  <div class="save-button">Save Battery</div>

  <div class="lower-panel"></div>
  <div class="charging">
    <svg width="34" height="20" viewBox="0 0 34 20"><rect x="1" y="3" width="28" height="15" rx="2" fill="none" stroke="#6ee81c" stroke-width="2"/><rect x="29" y="7" width="4" height="7" fill="#6ee81c"/><path d="M17 0 9 11h6l-3 9 9-12h-6z" fill="#6ee81c" stroke="#1a1a1a"/></svg>
    <p class="charging__label">Charging</p>
    <p class="charging__time">8hrs 15min</p>
  </div>

  <div class="shortcuts">
    <div class="shortcut">
      <div class="shortcut__icon"><svg width="24" height="24" viewBox="0 0 24 24"><circle cx="12" cy="12" r="10" fill="none" stroke="#6ee81c" stroke-width="2"/><path d="M12 12V3a9 9 0 0 1 8 13z" fill="#6ee81c"/></svg></div>
      Battery Status
    </div>
    <div class="shortcut">
      <div class="shortcut__icon"><svg width="24" height="16" viewBox="0 0 24 16"><rect x="1" y="1" width="19" height="14" rx="2" fill="#6ee81c"/><rect x="20" y="5" width="3" height="6" fill="#6ee81c"/><path d="M8 5 5 8l3 3M13 5l3 3-3 3" stroke="#111" fill="none" stroke-width="1.5"/></svg></div>
      Power Management
    </div>
    <div class="shortcut">
      <div class="shortcut__icon"><svg width="24" height="24" viewBox="0 0 24 24"><path d="M10 1h4l.6 3 2.4 1 2.6-1.7 2.8 2.8L20.7 8.7l1 2.3 2.3.6v4l-3 .6-1 2.4 1.7 2.6-2.8 2.8-2.6-1.7-2.4 1-.6 2.7h-4l-.6-3-2.4-1-2.6 1.7-2.8-2.8 1.7-2.6-1-2.4L0 14v-4l3-.6 1-2.4L2.3 4.4 5.1 1.6 7.7 3.3l2.4-1z" fill="#6ee81c"/><circle cx="12" cy="12" r="4" fill="#0c0c0c"/></svg></div>
      Settings
    </div>
  </div>

  <nav class="nav-bar">
    <svg width="12" height="10" viewBox="0 0 12 10"><path d="M0 1h12M0 5h12M0 9h12" stroke="#555" stroke-width="1.3"/></svg>
    <svg width="13" height="12" viewBox="0 0 13 12"><path d="M1 6 6.5 1 12 6M2.5 5v6h8V5" stroke="#555" fill="none" stroke-width="1.3"/></svg>
    <svg width="13" height="10" viewBox="0 0 13 10"><path d="M4 1 1 4l3 3M1 4h8a3 3 0 0 1 0 6" stroke="#555" fill="none" stroke-width="1.3"/></svg>
  </nav>
</section>

<!-- Power management screen -->
<section class="screen screen--power">
  <div class="status-bar">
    <svg width="12" height="10" viewBox="0 0 12 10"><rect x="3" y="1" width="6" height="8" rx="1" fill="none" stroke="#ccc"/><path d="M1 3v4M11 3v4" stroke="#ccc"/></svg>
    <svg width="12" height="10" viewBox="0 0 12 10"><path d="M0 10h2V7H0zM3 10h2V5H3zM6 10h2V3H6zM9 10h2V0H9z" fill="#39a0e0"/></svg>
    <svg width="7" height="11" viewBox="0 0 7 11"><rect x="0.5" y="1.5" width="6" height="9" fill="#39a0e0"/><rect x="2" y="0" width="3" height="2" fill="#39a0e0"/></svg>
    <svg width="11" height="11" viewBox="0 0 11 11"><circle cx="5.5" cy="6" r="4.3" fill="none" stroke="#ccc"/><path d="M5.5 3.5V6h2" stroke="#ccc" fill="none"/></svg>
    <span>00:22</span>
  </div>
  <header class="app-header">Charge Keeper Pro</header>
  <nav class="tabs">
    <span class="tab tab--clipped">RENT INFO</span>
    <span class="tab tab--active tab--after-clip">POWER MANAGEMENT</span>
  </nav>

  <ul class="settings-list">
    <li class="setting">
      <span class="setting__icon"><svg width="26" height="20" viewBox="0 0 26 20"><path d="M1 7a17 17 0 0 1 24 0M5 11a11 11 0 0 1 16 0M9 15a5 5 0 0 1 8 0" stroke="#6ee81c" stroke-width="2.4" fill="none" stroke-linecap="round"/><circle cx="13" cy="18" r="1.8" fill="#6ee81c"/></svg></span>
      <span class="setting__name">Wifi</span>
      <span class="toggle toggle--on">ON</span>
    </li>
    <li class="setting">
      <span class="setting__icon"><svg width="24" height="24" viewBox="0 0 24 24"><circle cx="12" cy="12" r="11" fill="#6ee81c"/><path d="M7 6c3 0 3 3 6 3s1 4-2 4-3 3-1 6M15 15c2 0 3 1 4 3" stroke="#1d1d1d" stroke-width="2" fill="none"/></svg></span>
      <span class="setting__name">Mobile data</span>
      <span class="toggle toggle--off">Off</span>
    </li>
    <li class="setting">
      <span class="setting__icon"><svg width="14" height="24" viewBox="0 0 14 24"><path d="M1 7l12 10-6 5V2l6 5L1 17" stroke="#6ee81c" stroke-width="2" fill="none"/></svg></span>
      <span class="setting__name">Bluetooth</span>
      <span class="toggle toggle--on">ON</span>
    </li>
    <li class="setting">
      <span class="setting__icon"><svg width="24" height="26" viewBox="0 0 24 26"><rect x="7" y="3" width="11" height="20" rx="2" transform="rotate(-15 12 13)" fill="none" stroke="#6ee81c" stroke-width="2"/><path d="M3 9 1 13l2 4M21 9l2 4-2 4" stroke="#6ee81c" stroke-width="1.6" fill="none"/></svg></span>
      <span class="setting__name">Vibrate</span>
      <span class="toggle toggle--off">Off</span>
    </li>
    <li class="setting">
      <span class="setting__icon"><svg width="26" height="26" viewBox="0 0 26 26"><circle cx="13" cy="13" r="6" fill="none" stroke="#6ee81c" stroke-width="2"/><path d="M13 8a5 5 0 0 1 0 10z" fill="#6ee81c"/><path d="M13 1v3M13 22v3M1 13h3M22 13h3M4.5 4.5l2 2M19.5 19.5l2 2M4.5 21.5l2-2M19.5 6.5l2-2" stroke="#6ee81c" stroke-width="2"/></svg></span>
      <div class="slider">
        <span class="slider__label">Brightness</span>
        <span class="slider__track"></span>
        <span class="slider__knob slider__knob--brightness"></span>
      </div>
    </li>
    <li class="setting">
      <span class="setting__icon"><svg width="26" height="22" viewBox="0 0 26 22"><path d="M2 7h5l6-5v18l-6-5H2z" fill="#6ee81c"/><path d="M16 7a5 5 0 0 1 0 8M19 4a9 9 0 0 1 0 14" stroke="#6ee81c" stroke-width="2" fill="none"/></svg></span>
      <div class="slider">
        <span class="slider__label">Volume</span>
        <span class="slider__track"></span>
        <span class="slider__knob slider__knob--volume"></span>
      </div>
    </li>
    <li class="setting">
      <span class="setting__icon"><svg width="26" height="26" viewBox="0 0 26 26"><circle cx="13" cy="13" r="7" fill="none" stroke="#6ee81c" stroke-width="2"/><path d="M13 9v8M9 13h8" stroke="#6ee81c" stroke-width="2"/><path d="M13 1v3M13 22v3M1 13h3M22 13h3M4.5 4.5l2 2M19.5 19.5l2 2M4.5 21.5l2-2M19.5 6.5l2-2" stroke="#6ee81c" stroke-width="2"/></svg></span>
      <span class="setting__name">Intelligent mode</span>
      <span class="toggle toggle--on">ON</span>
    </li>
  </ul>

  <nav class="nav-bar">
    <svg width="12" height="10" viewBox="0 0 12 10"><path d="M0 1h12M0 5h12M0 9h12" stroke="#555" stroke-width="1.3"/></svg>
    <svg width="13" height="12" viewBox="0 0 13 12"><path d="M1 6 6.5 1 12 6M2.5 5v6h8V5" stroke="#555" fill="none" stroke-width="1.3"/></svg>
    <svg width="13" height="10" viewBox="0 0 13 10"><path d="M4 1 1 4l3 3M1 4h8a3 3 0 0 1 0 6" stroke="#555" fill="none" stroke-width="1.3"/></svg>
  </nav>
</section>

</body>
</html>
```